Business Card for New Business

Please design a business card using our logo and font files. This is only one card for one person, as listed in details section.

Industry/Entity Type

Business

Contact Information for Business Card

Carl Voserby

Phone 555.318.6624
Cell 555.581.4096
Email carl@moltravex.com

www.moltravex.com

Address
18250 Brennick Lane #314
Halvern, VT 05619

Font styles to use
Sans Serif

Requirements
Must have
• Information listed in detail section. Must be standard card size.

```html
<!DOCTYPE html>
<html lang="en">
<head>
<meta charset="utf-8">
<title>Moltravex business card</title>
<link rel="stylesheet" href="https://fonts.googleapis.com/css2?family=Montserrat:wght@300;400;500;600&display=swap">
<style>
  :root {
    --backdrop: #e6e7e8;
    --paper: #ffffff;
    --ink: #000000;
    --accent: #c94e22;
    --text: #111111;
  }
  * { margin: 0; padding: 0; box-sizing: border-box; }
  html, body { width: 1200px; height: 927px; overflow: hidden; }
  body {
    background: var(--backdrop);
    font-family: "Montserrat", Arial, sans-serif;
    position: relative;
  }
  .card {
    position: absolute;
    top: 84px;
    width: 434px;
    height: 758px;
    border-radius: 30px;
    overflow: hidden;
  }
  .card--front { left: 144px; background: var(--paper); }
  .card--back { left: 622px; background: var(--ink); }

  .brand {
    position: absolute;
    left: 0; right: 0;
    display: flex;
    align-items: center;
    justify-content: center;
    gap: 12px;
  }
  .brand__dot {
    width: 40px; height: 40px;
    border-radius: 50%;
    background: var(--accent);
  }
  .brand__name {
    font-size: 60px;
    font-weight: 300;
    color: var(--accent);
    letter-spacing: 1px;
    line-height: 1;
  }
  .card--front .brand { top: 92px; }
  .card--back .brand { top: 310px; }

  .person-name {
    position: absolute;
    top: 303px; left: 0; right: 0;
    text-align: center;
    font-size: 36px;
    font-weight: 600;
    color: var(--accent);
    letter-spacing: 0.5px;
  }
  .rule {
    position: absolute;
    left: 76px;
    width: 280px;
    height: 2px;
    background: linear-gradient(90deg, transparent, var(--ink) 12%, var(--ink) 88%, transparent);
  }
  .rule--top { top: 478px; }
  .rule--bottom { top: 692px; }

  .details {
    position: absolute;
    left: 0; right: 0;
    text-align: center;
    font-size: 22px;
    font-weight: 400;
    color: var(--text);
    line-height: 24px;
  }
  .details--address { top: 491px; }
  .details--contact { top: 588px; }
  .accent { color: var(--accent); }

  .icons {
    position: absolute;
    top: 559px; left: 0; right: 0;
    display: flex;
    justify-content: center;
    gap: 8px;
  }
  .icons svg { width: 14px; height: 14px; }

  .back-url {
    position: absolute;
    top: 669px; left: 0; right: 0;
    text-align: center;
    font-size: 23px;
    color: var(--paper);
    letter-spacing: 1.5px;
  }

  .band {
    position: absolute;
    bottom: 0;
    height: 27px;
  }
  .band--left { left: 0; width: 212px; }
  .band--right { left: 220px; right: 0; background: var(--accent); }
  .card--front .band--left { background: var(--ink); }
  .card--back .band--left { background: var(--paper); }
</style>
</head>
<body>

<section class="card card--front" aria-label="Card front">
  <div class="brand"><span class="brand__dot"></span><span class="brand__name">moltravex</span></div>

  <h1 class="person-name">CARL VOSERBY</h1>

  <div class="rule rule--top"></div>
  <p class="details details--address">18250 Brennick Lane #314<br>Halvern, VT 05619</p>

  <div class="icons">
    <svg viewBox="0 0 16 16" aria-label="Phone"><path d="M4 2 L6 5 L5 7 C6 9 7 10 9 11 L11 10 L14 12 L12 14 C7 13 3 9 2 4 Z" fill="none" stroke="#c94e22" stroke-width="1.4"/></svg>
    <svg viewBox="0 0 16 16" aria-label="Mobile"><rect x="4.5" y="1.5" width="7" height="13" rx="1" fill="none" stroke="#c94e22" stroke-width="1.4"/><circle cx="8" cy="12" r="0.9" fill="#c94e22"/></svg>
    <svg viewBox="0 0 16 16" aria-label="Email"><rect x="1.5" y="3.5" width="13" height="9" fill="none" stroke="#c94e22" stroke-width="1.4"/><path d="M1.5 3.5 L8 9 L14.5 3.5" fill="none" stroke="#c94e22" stroke-width="1.4"/></svg>
    <svg viewBox="0 0 16 16" aria-label="Website"><circle cx="8" cy="8" r="6.3" fill="none" stroke="#c94e22" stroke-width="1.2"/><ellipse cx="8" cy="8" rx="2.8" ry="6.3" fill="none" stroke="#c94e22" stroke-width="1"/><path d="M1.7 8 H14.3 M2.8 4.8 H13.2 M2.8 11.2 H13.2" stroke="#c94e22" stroke-width="1"/></svg>
  </div>

  <p class="details details--contact">
    555.318.6624<br>
    555.581.4096<br>
    carl@moltravex.com<br>
    www.<span class="accent">moltravex</span>.com
  </p>
  <div class="rule rule--bottom"></div>

  <div class="band band--left"></div>
  <div class="band band--right"></div>
</section>

<section class="card card--back" aria-label="Card back">
  <div class="brand"><span class="brand__dot"></span><span class="brand__name">moltravex</span></div>
  <p class="back-url">www.<span class="accent">moltravex</span>.com</p>
  <div class="band band--left"></div>
  <div class="band band--right"></div>
</section>

</body>
</html>
```